New business card for Building services company

I own a small 1 person business which primarily works at heights. I gain access to my work areas via ladders and use safety harnesses. I conduct gutter cleaning, roof cleaning with a pressure cleaner(water blaster), ground level pressure cleaning (driveways, footpaths and walls), I also do small handy-man jobs & gardening/ tree trimming.

I have just had a logo designed by Sketch Hive, which I will upload. I'd like to see the themes followed through.
I like the colour of aqua or the colours what is in the logo.

I live in tropical north Queensland in Cairns, Australia. It is where the rain forest meets the Coral Lantern Shoal. On average it is 30+ degrees C.
Updates

Hello all designers. Thankyou for all the submissions so far. The following are my business details which I need on the card-

VERNO Roof, Gutter & Pressure Cleaning Services.
Director -Dale Marwick
Ph 0417385026
Email- roofcleaning@plovernet.example.au
ABN -48 902 317 254

Please include the following services which my business conducts-
*Gutter Cleaning
*Pressure Cleaning- Roof's, Driveways etc
*Minor Roof, Gutter & Building Maintenance
*Garden waste removal & complex cleanups

Public Liability upto $10 Million
Working at Heights Cert.

Quote-                                     Date-

Hi everyone,  could you please ensure you have -"Quote" and "Date" on the card. I'll need space to hand write details on the card for the specific details.        

Requirements
Must have
• The logo attached must be included.
• The rear side of the card is dedicated to job quoted and price of the job.
• *Please include- Quote price, Quote date. etc
• Including the tasks I do at work around the side of the card- Gutter Cleaning; Roof Cleaning, Gutter Maintenance; Gardening; Pressure Cleaning Roof's, Driveways etc.
Nice to have
• The rear side to have a ladder

```html
<!DOCTYPE html>
<html lang="en">
<head>
<meta charset="utf-8">
<title>VERNO Business Card</title>
<link href="https://fonts.googleapis.com/css2?family=Cinzel:wght@400;700&family=Kalam:wght@400&display=swap" rel="stylesheet">
<style>
  :root {
    --ink: #2a2a2a;
    --navy: #2c3590;
    --royal: #2b3a9a;
    --teal: #17a69a;
    --aqua: #1fb3a6;
    --green: #1f8a3a;
    --flash: #f2f6d8;
    --paper: #ffffff;
    --stage: #ffffff;
  }
  * { margin: 0; padding: 0; box-sizing: border-box; }
  html, body { width: 1200px; height: 1054px; overflow: hidden; background: var(--stage); }
  .canvas { position: relative; width: 1200px; height: 1054px; }

  .card {
    position: absolute;
    width: 420px;
    height: 240px;
    top: 75px;
    overflow: hidden;
  }

  /* Front */
  .card-front {
    left: 138px;
    background: var(--paper);
    box-shadow: 0 0 0 1px #e6e6e6;
  }
  .card-front .rule-top {
    position: absolute; left: 0; top: 0; width: 100%; height: 3px;
    background: linear-gradient(90deg, var(--navy) 0%, var(--teal) 70%, var(--green) 100%);
  }
  .card-front .band-bottom {
    position: absolute; left: 0; bottom: 0; width: 100%; height: 12px;
    background: linear-gradient(90deg, var(--navy) 0%, var(--royal) 25%, var(--teal) 60%, var(--aqua) 75%, var(--flash) 82%, var(--teal) 88%, var(--green) 100%);
  }
  .brand { position: absolute; left: 34px; top: 42px; }
  .brand-row { display: flex; align-items: center; gap: 8px; }
  .brand-name {
    font-family: 'Cinzel', serif; font-weight: 700; font-size: 30px;
    color: var(--navy); letter-spacing: 1px; line-height: 1;
  }
  .brand-dot { width: 13px; height: 13px; border-radius: 50%; background: var(--teal); }
  .brand-tagline {
    font-family: 'Cinzel', serif; font-size: 5.5px; color: var(--navy);
    letter-spacing: 0.2px; margin-top: 3px; text-transform: uppercase;
  }
  .services {
    position: absolute; left: 33px; top: 115px; list-style: none;
    font-family: 'Kalam', cursive; font-size: 13px; line-height: 17px;
    color: var(--ink);
  }
  .contact {
    position: absolute; right: 15px; top: 62px; width: 240px;
    text-align: right; font-family: 'Cinzel', serif; color: var(--ink);
  }
  .holder-name { font-size: 20px; line-height: 22px; }
  .holder-role { font-size: 8px; line-height: 10px; margin-top: 2px; }
  .call { font-weight: 700; font-size: 19px; line-height: 22px; margin-top: 34px; }
  .call small { font-size: 15px; }
  .details { font-size: 8px; line-height: 10px; margin-top: 28px; text-transform: none; }
  .details .email { font-family: Georgia, serif; letter-spacing: 0.2px; }

  /* Back */
  .card-back {
    left: 662px;
    background:
      linear-gradient(135deg, transparent 0 78%, rgba(250,252,225,0.85) 84%, rgba(255,255,255,0) 89%, transparent 100%),
      linear-gradient(125deg, var(--navy) 0%, var(--royal) 25%, #1e7fb0 48%, var(--teal) 65%, var(--aqua) 80%, var(--green) 100%);
  }
  .back-brand { position: absolute; left: 58px; top: 92px; color: var(--paper); }
  .back-brand .brand-name { color: var(--paper); font-size: 56px; font-weight: 400; letter-spacing: 1px; }
  .back-brand .brand-tagline { color: var(--paper); font-size: 7.5px; margin-top: 2px; }
  .back-call {
    font-family: 'Cinzel', serif; font-size: 12px; color: var(--paper);
    margin-left: 48px; margin-top: 1px;
  }
  .quote-fields {
    position: absolute; left: 58px; right: 40px; bottom: 22px;
    display: flex; gap: 24px;
    font-family: 'Cinzel', serif; font-size: 10px; color: var(--paper);
  }
  .quote-field { flex: 1; display: flex; align-items: flex-end; gap: 6px; }
  .quote-field .write-line { flex: 1; border-bottom: 1px solid rgba(255,255,255,0.8); height: 12px; }
</style>
</head>
<body>
<main class="canvas">
  <section class="card card-front" aria-label="Card front">
    <div class="rule-top"></div>
    <div class="brand">
      <div class="brand-row">
        <span class="brand-name">VERNO</span>
        <span class="brand-dot"></span>
      </div>
      <div class="brand-tagline">Roof, Gutter &amp; Pressure Cleaning Services</div>
    </div>
    <ul class="services">
      <li>-Roof Cleaning</li>
      <li>-Gutter Maintenance</li>
      <li>-Gardening</li>
      <li>-Pressure Cleaning Roof's</li>
      <li>-Driveways etc.</li>
    </ul>
    <div class="contact">
      <div class="holder-name">Dale Marwick</div>
      <div class="holder-role">Director</div>
      <div class="call"><small>CALL</small> 0417 385 026</div>
      <div class="details">
        <div class="email">roofcleaning@plovernet.example.au</div>
        <div>ABN 48 902 317 254 &middot; Cairns, Australia</div>
      </div>
    </div>
    <div class="band-bottom"></div>
  </section>

  <section class="card card-back" aria-label="Card back">
    <div class="back-brand">
      <div class="brand-name">VERNO</div>
      <div class="brand-tagline">Roof, Gutter &amp; Pressure Cleaning Services</div>
      <div class="back-call">CALL 0417 385 026</div>
    </div>
    <div class="quote-fields">
      <div class="quote-field"><span>Quote</span><span class="write-line"></span></div>
      <div class="quote-field"><span>Date</span><span class="write-line"></span></div>
    </div>
  </section>
</main>
</body>
</html>
```